US company needs luxury product packaging design for a line of hair extensions

What we Need:
Design product packaging for our top of the line hair extension product called Velorina™, the design should have the Velorina™ name,and the head from our Plumestrand logo on the box.

Who we are
Our company PlumeStrand™ is a wholesaler of 100% human hair extensions. We sell the best quality double drawn hair wefts, clip-ins and wigs.

The detailed brief is in the attached word document with examples of packaging we like and we have also uploaded our company logo

The winning designer(s) will work with us on 9 other products packages that we need, so it is important to think strategically

Thanks

Target Market(s)

African American Women

Industry/Entity Type

Hair And Beauty

Font styles to use
Serif
Decorative
Script

Colors
fbf289
b768aa
e24096
000000
fbd4d5
f59195
ffc214
d3a5cc
eda3c7

Requirements
Must have
• Evoke luxury
Nice to have
• See Attached brief

```html
<!DOCTYPE html>
<html lang="en">
<head>
<meta charset="utf-8">
<title>Drawer Slider Rigid Box – Dieline Layout</title>
<link href="https://fonts.googleapis.com/css2?family=Arimo:wght@400&display=swap" rel="stylesheet">
<style>
  :root{
    --canvas:#b4b4b4;
    --ink:#111111;
    --purple:#5c0a7e;
    --purple-mid:#3a0852;
    --purple-deep:#0b0012;
    --band-dark:#22002e;
    --paper:#ffffff;
    --panel-border:#4a4a4a;
    --name-ink:#f2e6f6;
    --fine-ink:#555555;
    --fine-light:#c9b9d4;
    --frame-line:#7a5a8e;
    --badge:#9c8aa6;
  }
  html,body{margin:0;padding:0;overflow:hidden;}
  body{width:1200px;height:1200px;background:var(--canvas);position:relative;}
  .spec-sheet{
    position:absolute;left:47px;top:232px;
    font-family:"Arimo",Arial,sans-serif;color:var(--ink);
    font-size:13.6px;line-height:18px;letter-spacing:.1px;
  }
  .spec-sheet .spec-title{font-size:16.5px;margin-bottom:4px;}
  .spec-sheet p{margin:0;}
  .dieline-art{position:absolute;left:0;top:0;}
  .product-name,.fine-print{font-family:"Arimo",Arial,sans-serif;font-weight:400;}
</style>
</head>
<body>

<section class="spec-sheet">
  <p class="spec-title">DRAWER SLIDER RIGID BOX (SMALL)</p>
  <p>CUSTOMER:&nbsp; ORVIEL2020 (MARKETLY)</p>
  <p>CAD DRAWING BUILT BY:</p>
  <p style="margin-top:2px">DALE MERCER (www.foldlinestudio.com)</p>
  <p>DATE COMPLETED:&nbsp; 14 SEPT 2016</p>
  <p>STYLE:&nbsp; CUSTOM RIGID BOX</p>
  <p>SIZE:&nbsp; DRAWER - 6" X 5" X 2"</p>
  <p style="margin-top:2px">SLEEVE - 6.125" X 2.125" X 5.125"</p>
  <p>MATERIAL:&nbsp; .060 GAUGE PAPERBOARD THICKNESS</p>
</section>

<svg class="dieline-art" width="1200" height="1200" viewBox="0 0 1200 1200" xmlns="http://www.w3.org/2000/svg">
  <defs>
    <linearGradient id="fade-left" x1="0" x2="1" y1="0" y2="0">
      <stop offset="0" stop-color="var(--purple-deep)"/><stop offset="1" stop-color="var(--purple)"/>
    </linearGradient>
    <linearGradient id="fade-right" x1="1" x2="0" y1="0" y2="0">
      <stop offset="0" stop-color="var(--purple-deep)"/><stop offset="1" stop-color="var(--purple)"/>
    </linearGradient>
    <linearGradient id="fade-top" x1="0" x2="0" y1="0" y2="1">
      <stop offset="0" stop-color="var(--purple-deep)"/><stop offset="1" stop-color="var(--purple)"/>
    </linearGradient>
    <linearGradient id="fade-bottom" x1="0" x2="0" y1="1" y2="0">
      <stop offset="0" stop-color="var(--purple-deep)"/><stop offset="1" stop-color="var(--purple)"/>
    </linearGradient>
    <linearGradient id="sleeve-panel" x1="0" x2="0" y1="0" y2="1">
      <stop offset="0" stop-color="#050008"/><stop offset="1" stop-color="var(--purple-mid)"/>
    </linearGradient>
    <linearGradient id="sleeve-band" x1="0" x2="0" y1="0" y2="1">
      <stop offset="0" stop-color="#12001a"/><stop offset="1" stop-color="var(--purple-mid)"/>
    </linearGradient>
    <radialGradient id="portrait-tone" cx=".5" cy=".45" r=".6">
      <stop offset="0" stop-color="#e0306e"/><stop offset="1" stop-color="#8a1050"/>
    </radialGradient>
  </defs>

  <!-- Drawer outer wrap -->
  <g class="drawer-wrap">
    <rect x="562" y="290" width="151" height="266" fill="var(--purple)"/>
    <polygon points="562,290 713,290 713,354 562,354" fill="url(#fade-top)"/>
    <polygon points="562,492 713,492 713,556 562,556" fill="url(#fade-bottom)"/>
    <polygon points="491,341 555,341 562,353 562,494 555,506 491,506" fill="url(#fade-left)"/>
    <polygon points="783,341 720,341 713,353 713,494 720,506 783,506" fill="url(#fade-right)"/>
  </g>

  <!-- Drawer inner tray -->
  <g class="drawer-tray">
    <rect x="926" y="319" width="150" height="211" fill="var(--paper)"/>
    <rect x="883" y="362" width="235" height="124" fill="var(--paper)"/>
    <rect x="926" y="319" width="150" height="23" fill="var(--band-dark)"/>
    <rect x="926" y="508" width="150" height="22" fill="var(--band-dark)"/>
    <rect x="883" y="362" width="22" height="124" fill="var(--band-dark)"/>
    <rect x="1098" y="362" width="20" height="124" fill="var(--band-dark)"/>
    <rect x="928" y="364" width="146" height="121" rx="4" fill="var(--paper)" stroke="var(--panel-border)" stroke-width="1.6"/>
    <g class="fine-print" fill="var(--fine-ink)" font-size="3.2" text-anchor="middle">
      <g transform="rotate(180 1001 390)">
        <line x1="962" y1="379" x2="1040" y2="379" stroke="var(--fine-ink)" stroke-width=".4"/>
        <text x="1001" y="384">Velorina™ is our finest collection of 100%</text>
        <text x="1001" y="388">human hair, soft and full from root to end.</text>
        <text x="1001" y="392">Each bundle is sorted and sewn with care.</text>
        <text x="1001" y="396">Wash gently and let it air dry for best</text>
        <text x="1001" y="400">results. Style with low heat only.</text>
        <line x1="962" y1="403" x2="1040" y2="403" stroke="var(--fine-ink)" stroke-width=".4"/>
        <text x="1001" y="408">CARE GUIDE</text>
      </g>
      <text x="1001" y="445">ABOUT VELORINA</text>
      <line x1="962" y1="448" x2="1040" y2="448" stroke="var(--fine-ink)" stroke-width=".4"/>
      <text x="1001" y="453">Velorina™ is our most luxurious, high quality, 100%</text>
      <text x="1001" y="457">human hair, cut and sorted with the cuticle intact.</text>
      <text x="1001" y="461">Each weft is sewn by hand to hold its shape</text>
      <text x="1001" y="465">and comes in different textures, lengths and colors.</text>
      <text x="1001" y="469">Velorina™ can be dyed, bleached or curled with</text>
      <text x="1001" y="473">ease, and stays soft wash after wash.</text>
      <line x1="962" y1="477" x2="1040" y2="477" stroke="var(--fine-ink)" stroke-width=".4"/>
    </g>
  </g>

  <!-- Sleeve -->
  <g class="sleeve">
    <polygon points="220,657 404,657 404,788 394,798 230,798 220,788" fill="url(#sleeve-panel)"/>
    <polygon points="230,852 394,852 404,862 404,995 220,995 220,862" fill="url(#sleeve-panel)"/>
    <rect x="94" y="798" width="436" height="54" fill="url(#sleeve-band)"/>

    <!-- back panel -->
    <rect x="239" y="674" width="147" height="122" fill="none" stroke="var(--frame-line)" stroke-width=".7"/>
    <text class="product-name" x="312" y="731" text-anchor="middle" font-size="15" fill="var(--name-ink)">Lumera</text>
    <text class="fine-print" x="312" y="740" text-anchor="middle" font-size="3.2" fill="var(--fine-light)">100% HUMAN HAIR EXTENSIONS</text>
    <line x1="266" y1="768" x2="358" y2="768" stroke="var(--fine-light)" stroke-width=".5"/>
    <g class="fine-print" font-size="2.8" fill="var(--fine-light)" text-anchor="middle">
      <text x="312" y="775">Product of Plumestrand LLC. All rights reserved.</text>
      <text x="312" y="779">Lumera name and Plumestrand are trademarks of Plumestrand</text>
      <text x="312" y="783">LLC., registered in the USA.</text>
    </g>
    <line x1="266" y1="789" x2="358" y2="789" stroke="var(--fine-light)" stroke-width=".5"/>

    <!-- front panel -->
    <path d="M312 880 C342 880 360 905 356 930 L352 944 L276 944 L272 930 C268 905 284 880 312 880 Z"
          fill="url(#portrait-tone)" role="img" aria-label="Illustrated profile head from the PlumeStrand brand artwork, in magenta tones"/>
    <text class="product-name" x="312" y="959" text-anchor="middle" font-size="13" fill="var(--name-ink)">Lumera</text>
    <text class="fine-print" x="312" y="965" text-anchor="middle" font-size="3" fill="var(--fine-light)">100% Human Hair Extensions</text>
    <line x1="272" y1="970" x2="352" y2="970" stroke="var(--fine-light)" stroke-width=".5"/>

    <!-- side flaps -->
    <text class="product-name" x="180" y="829" text-anchor="middle" font-size="12" fill="var(--name-ink)">Lumera</text>
    <text class="fine-print" x="180" y="837" text-anchor="middle" font-size="3.2" fill="var(--fine-light)">100% Human Hair Extensions</text>
    <text class="product-name" x="444" y="829" text-anchor="middle" font-size="12" fill="var(--name-ink)">Lumera</text>
    <text class="fine-print" x="444" y="837" text-anchor="middle" font-size="3.2" fill="var(--fine-light)">100% Human Hair Extensions</text>

    <rect x="115" y="804" width="7" height="7" fill="var(--badge)"/>
    <rect x="124" y="804" width="5" height="7" fill="var(--badge)"/>
    <circle cx="122" cy="842" r="4.5" fill="var(--badge)"/>
    <rect x="496" y="804" width="7" height="7" fill="var(--badge)"/>
    <rect x="505" y="804" width="5" height="7" fill="var(--badge)"/>
    <circle cx="503" cy="842" r="4.5" fill="var(--badge)"/>
  </g>

  <!-- Blank board cross -->
  <g class="board-blank" fill="var(--paper)">
    <rect x="782" y="670" width="153" height="296"/>
    <rect x="661" y="792" width="393" height="53"/>
  </g>
</svg>

</body>
</html>
```